Bref créative
Business Cards - Skyline Assessors
Two sided business cards
Simple
Corwin Hask
Certified Appraiser
48270 Millbrook Lane #1174
Sterling, VA 20391
corwin@plumvexa.com
www.plumvexa.com
Just the logo, either include the text or not (what ever looks better)
Colors and Fonts Guide

```html
<!DOCTYPE html>
<html lang="en">
<head>
<meta charset="utf-8">
<title>Skyline Assessors – Business Cards</title>
<link rel="stylesheet" href="https://fonts.googleapis.com/css2?family=Roboto:wght@400;500;700&display=swap">
<style>
  :root {
    --bg: #ece7e1;
    --card-white: #ffffff;
    --navy: #1f3557;
    --navy-deep: #0b1a33;
    --navy-glow: #3f7bb0;
    --band-light: #dfe3e9;
    --brand-red: #8c1d24;
    --ink: #2a2a2a;
    --muted: #555555;
    --rule: #9a9a9a;
  }
  * { box-sizing: border-box; margin: 0; padding: 0; }
  html, body { width: 1200px; height: 730px; overflow: hidden; }
  body {
    background: var(--bg);
    font-family: "Roboto", Arial, sans-serif;
    color: var(--ink);
    position: relative;
  }
  .card {
    position: absolute;
    width: 500px;
    height: 290px;
    border-radius: 20px;
    box-shadow: 0 3px 10px rgba(0,0,0,.18);
    overflow: hidden;
  }
  .card--front { left: 70px; top: 45px; background: var(--card-white); }
  .card--back-light { left: 630px; top: 45px; background: var(--card-white); }
  .card--back-dark {
    left: 350px; top: 385px;
    background: radial-gradient(ellipse at 50% 35%, var(--navy-glow) 0%, var(--navy) 40%, var(--navy-deep) 82%);
  }

  /* header band */
  .band {
    position: absolute; left: 0; right: 0;
    border-radius: 6px;
  }
  .band--navy {
    top: 58px; height: 12px;
    background: linear-gradient(90deg, rgba(31,53,87,0) 0%, var(--navy) 22%, var(--navy) 78%, rgba(31,53,87,0) 100%);
  }
  .band--navy-thin {
    top: 78px; height: 3px; left: 60px; right: 60px;
    background: linear-gradient(90deg, rgba(63,123,176,0) 0%, var(--navy-glow) 50%, rgba(63,123,176,0) 100%);
  }
  .band--grey {
    top: 58px; height: 12px;
    background: linear-gradient(90deg, rgba(223,227,233,0) 0%, var(--band-light) 22%, var(--band-light) 78%, rgba(223,227,233,0) 100%);
  }
  .band--grey-thin {
    top: 78px; height: 3px; left: 60px; right: 60px;
    background: linear-gradient(90deg, rgba(223,227,233,0) 0%, var(--band-light) 50%, rgba(223,227,233,0) 100%);
  }

  .holder {
    position: absolute; top: 18px; right: 40px;
    display: flex; align-items: center; gap: 10px;
  }
  .holder__name { font-size: 24px; font-weight: 700; color: var(--ink); }
  .holder__divider { width: 1px; height: 20px; background: var(--rule); }
  .holder__title { font-size: 13px; font-weight: 500; color: var(--ink); }

  .brand-name {
    position: absolute;
    font-weight: 700;
    letter-spacing: 3px;
    text-transform: uppercase;
    line-height: 1.1;
    text-align: center;
  }
  .brand-name__line { display: block; }
  .card--front .brand-name { left: 22px; top: 168px; width: 240px; font-size: 27px; color: var(--brand-red); }
  .card--back-light .brand-name { right: 22px; top: 168px; width: 240px; font-size: 27px; color: var(--brand-red); }
  .card--back-dark .brand-name { left: 0; right: 0; top: 112px; font-size: 38px; color: #ffffff; }
  .dark-rule {
    position: absolute; left: 110px; right: 110px; top: 160px; height: 1px;
    background: rgba(255,255,255,.55);
  }

  .contact {
    position: absolute; left: 290px; top: 182px;
    list-style: none; font-size: 11.5px; color: var(--muted); line-height: 16px;
  }
  .contact__item { display: flex; align-items: center; gap: 7px; }
  .contact__item--address { display: block; margin-bottom: 6px; }
  .contact__icon { width: 8px; height: 8px; flex: none; }

  .site {
    position: absolute; display: flex; align-items: center; gap: 7px;
    font-size: 12.5px; font-weight: 700;
  }
  .card--back-light .site { left: 30px; bottom: 20px; color: var(--ink); }
  .card--back-dark .site { left: 0; right: 0; top: 228px; justify-content: center; color: #d7e2ef; font-weight: 400; }
  .site__dot { width: 7px; height: 7px; border-radius: 50%; background: currentColor; }
</style>
</head>
<body>

  <section class="card card--front" aria-label="Business card front">
    <div class="holder">
      <span class="holder__name">Corwin Hask</span>
      <span class="holder__divider"></span>
      <span class="holder__title">Certified Appraiser</span>
    </div>
    <div class="band band--navy"></div>
    <div class="band band--navy-thin"></div>
    <div class="brand-name"><span class="brand-name__line">Skyline</span><span class="brand-name__line">Assessors</span></div>
    <ul class="contact">
      <li class="contact__item contact__item--address">48270 Millbrook Lane #1174<br>Sterling, VA 20391</li>
      <li class="contact__item">
        <svg class="contact__icon" viewBox="0 0 10 10"><circle cx="5" cy="5" r="4.5" fill="#1f3557"/></svg>
        3015550142
      </li>
      <li class="contact__item">
        <svg class="contact__icon" viewBox="0 0 10 10"><circle cx="5" cy="5" r="4.5" fill="#1f3557"/></svg>
        corwin@plumvexa.com
      </li>
      <li class="contact__item">
        <svg class="contact__icon" viewBox="0 0 10 10"><circle cx="5" cy="5" r="4.5" fill="#1f3557"/></svg>
        www.plumvexa.com
      </li>
    </ul>
  </section>

  <section class="card card--back-light" aria-label="Business card back, light">
    <div class="band band--grey"></div>
    <div class="band band--grey-thin"></div>
    <div class="brand-name"><span class="brand-name__line">Skyline</span><span class="brand-name__line">Assessors</span></div>
    <div class="site"><span class="site__dot"></span>www.plumvexa.com</div>
  </section>

  <section class="card card--back-dark" aria-label="Business card back, dark">
    <div class="brand-name">Skyline Assessors</div>
    <div class="dark-rule"></div>
    <div class="site"><span class="site__dot"></span>www.plumvexa.com</div>
  </section>

</body>
</html>
```